Management Consulting and Executive Coaching business needs a brochure.

I need a brochure that I can send to prospective clients. I provide management consulting services and executive coaching supports targeting organizations focused on social impact. I would like to see designs that use vibrant colors consistent with my logo (see attached) and that communicate forward motion/progress.

Target Market(s)

Social Impact leaders and organizations

Industry/Entity Type

Management Consulting

Font styles to use
Serif

Colors
b29ec9
85acd3
86cae7
87d0c7
acd037

Requirements
Must have
• Must have exciting, colorful, design features using words, art, imagery.
Should not have
• No dark or depressing imagery

```html
<!DOCTYPE html>
<html lang="en">
<head>
<meta charset="utf-8">
<title>Larkfield Partners – Brochure</title>
<link rel="stylesheet" href="https://fonts.googleapis.com/css2?family=Libre+Baskerville:ital,wght@0,400;0,700;1,400&family=Montserrat:wght@400;500;600&display=swap">
<style>
  :root{
    --stage:#e2d8d3;
    --paper:#ffffff;
    --teal:#86c9bf;
    --teal-deep:#5e9f97;
    --ink:#3a3a3a;
    --muted:#666;
    --title-blue:#2d5aa0;
    --brand-blue:#2f8fc4;
    --photo-a:#c9b9a6;
    --photo-b:#8c8c86;
    --photo-c:#e6e3de;
    --photo-d:#a6a39b;
  }
  *{box-sizing:border-box;margin:0;padding:0}
  html,body{width:1200px;height:2437px;overflow:hidden;background:var(--stage)}
  body{font-family:"Montserrat",sans-serif;color:var(--ink)}
  .scene{position:relative;width:1200px;height:812px;background:var(--stage);overflow:hidden}
  .scene--last{height:813px}

  /* ---------- cover ---------- */
  .cover{position:absolute;width:500px;height:707px;background:var(--paper);overflow:hidden;box-shadow:0 10px 24px rgba(0,0,0,.12)}
  .cover__brand{position:absolute;top:38px;left:0;right:0;text-align:center;display:flex;justify-content:center;align-items:center;gap:10px}
  .brand-dot{width:16px;height:16px;border-radius:50%;background:var(--brand-blue)}
  .brand-name{font-family:"Libre Baskerville",serif;font-weight:400;font-size:26px;letter-spacing:3px;color:var(--brand-blue)}
  .cover__band{position:absolute;left:0;right:0;top:320px;bottom:0;background:linear-gradient(180deg,var(--teal) 0%,var(--teal-deep) 100%)}
  .cover__photo{position:absolute;left:44px;top:102px;width:412px;height:300px;border:7px solid var(--paper);background:linear-gradient(135deg,var(--photo-a),var(--photo-c) 45%,var(--photo-b))}
  .cover__title{position:absolute;left:0;right:0;top:450px;text-align:center;font-family:"Libre Baskerville",serif;font-weight:700;font-size:25px;line-height:1.3;color:#fff;text-transform:uppercase;letter-spacing:.5px}
  .cover__web{position:absolute;left:0;right:0;top:560px;text-align:center;font-size:12px;color:#fff;letter-spacing:.5px}

  /* ---------- back cover ---------- */
  .back{position:absolute;width:500px;height:707px;background:var(--paper);overflow:hidden;box-shadow:0 10px 24px rgba(0,0,0,.12)}
  .back__band{position:absolute;left:0;right:0;bottom:0;height:300px}
  .back__brand{position:absolute;left:34px;bottom:102px;width:180px;display:flex;align-items:center;gap:10px}
  .back__brand .brand-dot{background:#fff;width:13px;height:13px}
  .back__brand .brand-name{color:#fff;font-size:17px;letter-spacing:2px;line-height:1.25}
  .back__divider{position:absolute;left:226px;bottom:62px;width:1px;height:160px;background:rgba(255,255,255,.7)}
  .contact{position:absolute;left:242px;bottom:66px;width:236px;list-style:none;color:#fff}
  .contact li{display:flex;align-items:center;gap:9px;font-size:10.5px;line-height:1.35;margin-top:10px}
  .contact li:first-child{font-size:15px;font-weight:600}
  .contact svg{flex:none;width:20px;height:20px}

  .spread-small{position:absolute;left:180px;top:109px;width:1000px;height:707px;transform:scale(.84);transform-origin:0 0}

  /* ---------- inner spread ---------- */
  .page{position:absolute;top:66px;width:480px;height:680px;background:var(--paper);overflow:hidden;box-shadow:0 10px 24px rgba(0,0,0,.12)}
  .page--left{left:120px}
  .page--right{left:600px;background:linear-gradient(90deg,#ececec,#fff 14%)}
  .page__strip{position:absolute;left:0;top:0;bottom:0;width:110px;background:var(--teal)}
  .page__photo{position:absolute;border:6px solid var(--paper);background:linear-gradient(135deg,var(--photo-c),var(--photo-d) 60%,var(--photo-b))}
  .page--left .page__photo{left:40px;top:28px;width:410px;height:268px}
  .page--right .page__photo{left:40px;top:36px;width:400px;height:252px;border:none}
  .company{position:absolute;left:140px;top:320px;font-family:"Libre Baskerville",serif;font-weight:700;font-size:17px;color:var(--title-blue);text-transform:uppercase}
  .tag{display:inline-block;border:1px solid var(--ink);padding:5px 12px;font-family:"Libre Baskerville",serif;font-weight:700;font-size:13px;color:var(--title-blue);text-transform:uppercase}
  .about{position:absolute;left:140px;top:362px;width:310px}
  .about p{margin-top:14px;font-size:9.5px;line-height:1.55;color:var(--muted);text-align:justify}
  .page__rule{position:absolute;left:140px;right:30px;bottom:48px;height:1px;background:#bbb}
  .page__num{position:absolute;right:30px;bottom:28px;font-size:8px;color:#777}
  .page--right .page__rule{left:30px}
  .services{position:absolute;left:36px;top:318px;right:26px}
  .services__cols{display:flex;gap:18px;margin-top:18px}
  .svc--main{width:238px;flex:none}
  .svc--side{flex:1;padding-top:52px}
  .svc h3{display:flex;align-items:center;gap:8px;font-family:"Libre Baskerville",serif;font-weight:700;font-size:10.5px;color:var(--title-blue);text-transform:uppercase;margin-top:10px;white-space:nowrap}
  .svc-icon{width:22px;height:22px;border-radius:50%;background:var(--teal);flex:none}
  .ticks{list-style:none;margin:6px 0 0 30px}
  .ticks li{position:relative;padding-left:14px;font-size:9px;line-height:1.4;margin-top:4px;color:var(--ink)}
  .ticks li::before{content:"";position:absolute;left:0;top:3px;width:7px;height:7px;border:1px solid var(--teal-deep);border-radius:50%}
  .ticks--side{margin-left:0}
</style>
</head>
<body>

<!-- front cover -->
<section class="scene">
  <article class="cover" style="left:350px;top:52px">
    <div class="cover__band"></div>
    <div class="cover__brand"><span class="brand-dot"></span><span class="brand-name">LARKFIELD PARTNERS</span></div>
    <div class="cover__photo" role="img" aria-label="Photo of three colleagues reviewing work on a laptop in a bright office"></div>
    <h1 class="cover__title">Management Consulting<br>and Executive Coaching</h1>
    <p class="cover__web">www.larkfieldpartners.com</p>
  </article>
</section>

<!-- back and front covers -->
<section class="scene">
  <div class="spread-small">
    <article class="back" style="left:0;top:0">
      <svg class="back__band" viewBox="0 0 500 300" preserveAspectRatio="none">
        <defs><linearGradient id="bandGrad" x1="0" y1="0" x2="0" y2="1"><stop offset="0" stop-color="#86c9bf"/><stop offset="1" stop-color="#5e9f97"/></linearGradient></defs>
        <path d="M0 70 Q250 70 500 0 L500 300 L0 300 Z" fill="url(#bandGrad)"/>
      </svg>
      <div class="back__brand"><span class="brand-dot"></span><span class="brand-name">LARKFIELD<br>PARTNERS</span></div>
      <div class="back__divider"></div>
      <ul class="contact">
        <li><svg viewBox="0 0 20 20"><circle cx="10" cy="10" r="9" fill="none" stroke="#fff"/><path d="M7 6l2 2-1 1a5 5 0 003 3l1-1 2 2-1.5 1.5C9 14 6 11 5.5 7.5z" fill="#fff"/></svg>555-014-2290</li>
        <li><svg viewBox="0 0 20 20"><circle cx="10" cy="10" r="9" fill="none" stroke="#fff"/><path d="M10 5a3 3 0 013 3c0 2.5-3 6-3 6s-3-3.5-3-6a3 3 0 013-3z" fill="#fff"/><circle cx="10" cy="8" r="1" fill="#5e9f97"/></svg><span>48 Alder Lane | Brookvale,<br>CA 90001</span></li>
        <li><svg viewBox="0 0 20 20"><circle cx="10" cy="10" r="9" fill="none" stroke="#fff"/><rect x="5.5" y="7" width="9" height="6" fill="none" stroke="#fff"/><path d="M5.5 7l4.5 3.5L14.5 7" fill="none" stroke="#fff"/></svg>hello@larkfieldpartners.com</li>
        <li><svg viewBox="0 0 20 20"><circle cx="10" cy="10" r="9" fill="none" stroke="#fff"/><circle cx="10" cy="10" r="4.5" fill="none" stroke="#fff"/><path d="M5.5 10h9M10 5.5c-2 3-2 6 0 9M10 5.5c2 3 2 6 0 9" fill="none" stroke="#fff" stroke-width=".8"/></svg>www.larkfieldpartners.com</li>
      </ul>
    </article>
    <article class="cover" style="left:500px;top:0">
      <div class="cover__band"></div>
      <div class="cover__brand"><span class="brand-dot"></span><span class="brand-name">LARKFIELD PARTNERS</span></div>
      <div class="cover__photo" role="img" aria-label="Photo of three colleagues reviewing work on a laptop in a bright office"></div>
      <h1 class="cover__title">Management Consulting<br>and Executive Coaching</h1>
      <p class="cover__web">www.larkfieldpartners.com</p>
    </article>
  </div>
</section>

<!-- inner spread -->
<section class="scene scene--last">
  <article class="page page--left">
    <div class="page__strip"></div>
    <div class="page__photo" role="img" aria-label="Photo of a smiling team leader handing papers to colleagues at a meeting table"></div>
    <h2 class="company">Larkfield Partners LLC</h2>
    <div class="about">
      <span class="tag">About Us</span>
      <p>Larkfield Partners LLC was formed based on the belief that promoting diverse perspectives leads to better solutions. The colors of the lark's many feathers represent the beauty that is created by diverse colors. Independently, the colors are lovely, and together the colors present a spectacular and beautiful palate. We promote diversity of thought, action, and inclusion.</p>
      <p>We believe that high performing leaders create and lead high performing organizations. We seek to partner with leaders and organizations across sectors who share a vision and mission to make a positive impact in the community.</p>
    </div>
    <div class="page__rule"></div>
    <span class="page__num">Page 2</span>
  </article>

  <article class="page page--right">
    <div class="page__photo" role="img" aria-label="Photo of a diverse team in discussion around a table in a bright room with plants"></div>
    <div class="services">
      <span class="tag">Our Services</span>
      <div class="services__cols">
        <div class="svc svc--main">
          <h3><span class="svc-icon"></span>Executive Coaching</h3>
          <ul class="ticks"><li>1:1 Coaching to achieve personal and professional goals</li></ul>
          <h3><span class="svc-icon"></span>Management Consulting</h3>
          <ul class="ticks">
            <li>Strategic planning</li>
            <li>Board/executive team development</li>
            <li>Diversity training</li>
            <li>Program development and sustainability</li>
          </ul>
        </div>
        <div class="svc svc--side">
          <ul class="ticks ticks--side">
            <li>Group Coaching</li>
          </ul>
          <ul class="ticks ticks--side" style="margin-top:30px">
            <li>Management &amp; leadership training</li>
            <li>Moderating/MC/Keynote Speaker (topics - leadership, mission-driven philanthropy, social justice, motivational)</li>
            <li>Facilitation - retreats, team planning, analysis &amp; problem solving.</li>
          </ul>
        </div>
      </div>
    </div>
    <div class="page__rule"></div>
    <span class="page__num">Page 3</span>
  </article>
</section>

</body>
</html>
```